Business Card design for construction company

I would like a business card design for a construction company - Harlow Constructions. I have attached the ai logo file for use. I would like the card to be very smart and clean and incorporate only white and the two colours in the logo. I would like the card to have two sides. One side can just have the logo, the other with the relevant information.

Target Market(s)

Building and Construction Clients

Industry/Entity Type

Business

Contact Information for Business Card

Name: Tom Pardoe
Company: Harlow Constructions Pty Limited
Address: 14 Mallee Crescent Carrow Vale 2093
Phone: 0427 531 068
Email: tomp@harlowbuild-example.com.au

Font styles to use
Serif
Sans Serif

Requirements
Must have
• Details noted above
• Logo as provided
• Colours as in logo
• Square edges
• A font that compliments the logo
Should not have
• Any colour other than white and those in logo
• Rounded edges

```html
<!DOCTYPE html>
<html lang="en">
<head>
<meta charset="utf-8">
<title>Harlow Constructions – Business Card</title>
<link rel="stylesheet" href="https://fonts.googleapis.com/css2?family=Open+Sans:wght@400;600;700&display=swap">
<style>
  :root {
    --bg: #e4e5e7;
    --card: #ffffff;
    --ink: #3b3e43;
    --icon: #777777;
    --blue-1: #0ea5ea;
    --blue-2: #2fb6f0;
    --blue-3: #5cc8f5;
    --blue-4: #8fdaf9;
    --aqua-1: #1ed0f5;
    --aqua-2: #5edcf8;
    --aqua-3: #8fe6fa;
  }
  * { box-sizing: border-box; margin: 0; padding: 0; }
  html, body {
    width: 1200px; height: 800px; overflow: hidden;
    background: var(--bg);
    font-family: "Open Sans", Arial, sans-serif;
    color: var(--ink);
  }
  .stage {
    width: 1200px; height: 800px;
    display: flex; align-items: center; justify-content: center; gap: 40px;
  }
  .card {
    position: relative;
    width: 540px; height: 310px;
    background: var(--card);
    overflow: hidden;
    box-shadow: 0 10px 24px rgba(0,0,0,0.12);
  }
  .stripes { position: absolute; top: 0; bottom: 0; display: flex; }
  .stripes span { display: block; height: 100%; }

  /* Front */
  .card--front .stripes { right: 0; }
  .card--front .stripes span:nth-child(1) { width: 34px; background: var(--aqua-3); }
  .card--front .stripes span:nth-child(2) { width: 30px; background: var(--aqua-2); }
  .card--front .stripes span:nth-child(3) { width: 46px; background: var(--aqua-1); }
  .card--front .wordmark { position: absolute; left: 40px; top: 126px; }

  /* Back */
  .card--back .stripes { left: 0; }
  .card--back .stripes span:nth-child(1) { width: 36px; background: var(--blue-1); }
  .card--back .stripes span:nth-child(2) { width: 18px; background: var(--blue-2); }
  .card--back .stripes span:nth-child(3) { width: 16px; background: var(--blue-3); }
  .card--back .stripes span:nth-child(4) { width: 14px; background: var(--blue-4); }
  .card--back .wordmark { position: absolute; left: 116px; top: 48px; }

  .wordmark {
    display: flex; align-items: center; gap: 10px;
    font-weight: 400; font-size: 19px; letter-spacing: 3px;
    text-transform: uppercase; color: var(--ink); white-space: nowrap;
    line-height: 1;
  }
  .wordmark .mark { width: 9px; height: 9px; background: var(--blue-1); flex: none; }

  .contact { position: absolute; left: 170px; top: 130px; }
  .contact .name { font-size: 15px; font-weight: 700; text-transform: uppercase; }
  .contact .company { font-size: 13px; font-weight: 600; margin-bottom: 16px; }
  .contact ul { list-style: none; }
  .contact li {
    display: flex; align-items: center; gap: 10px;
    font-size: 13px; font-weight: 600; line-height: 22px;
  }
  .contact svg { width: 11px; height: 11px; flex: none; }
</style>
</head>
<body>
  <main class="stage">
    <section class="card card--front" aria-label="Business card front">
      <div class="wordmark"><span class="mark"></span>Harlow Constructions</div>
      <div class="stripes"><span></span><span></span><span></span></div>
    </section>

    <section class="card card--back" aria-label="Business card back">
      <div class="stripes"><span></span><span></span><span></span><span></span></div>
      <div class="wordmark"><span class="mark"></span>Harlow Constructions</div>
      <div class="contact">
        <p class="name">Tom Pardoe</p>
        <p class="company">Harlow Constructions Pty Limited</p>
        <ul>
          <li>
            <svg viewBox="0 0 12 12" aria-hidden="true"><path d="M6 1a3.5 3.5 0 0 0-3.5 3.5C2.5 7 6 11 6 11s3.5-4 3.5-6.5A3.5 3.5 0 0 0 6 1z" fill="none" stroke="#777" stroke-width="1.2"/><circle cx="6" cy="4.5" r="1.2" fill="#777"/></svg>
            14 Mallee Crescent Carrow Vale 2093
          </li>
          <li>
            <svg viewBox="0 0 12 12" aria-hidden="true"><path d="M3 1.5l2 2.2-1.2 1.3a7 7 0 0 0 3.2 3.2L8.3 7l2.2 2-1.3 1.5C5.5 10.5 1.5 6.5 1.5 2.8z" fill="none" stroke="#777" stroke-width="1.1" stroke-linejoin="round"/></svg>
            0427 531 068
          </li>
          <li>
            <svg viewBox="0 0 12 12" aria-hidden="true"><rect x="1" y="2.5" width="10" height="7" fill="none" stroke="#777" stroke-width="1.1"/><path d="M1 2.5l5 4 5-4" fill="none" stroke="#777" stroke-width="1.1"/></svg>
            tomp@harlowbuild-example.com.au
          </li>
        </ul>
      </div>
    </section>
  </main>
</body>
</html>
```